Brevik Plant Traders Company - Enhance our webpage

We have an existing website - please see www.brockwaytooling.com. The text in there is fundamentally what we want to say. There is also a search function where you can search our database, which is crucial to the site. We are happy with our logo, top left-hand side and want it to remain as it is. Everything else, including pictures, drawings and animation can be changed. In general, the website looks a little tired and the icons on the tabs need creative input.

We want our website to look dynamic, eye-catching, bold, very professional, modern and also uphold our impeccable 30-year reputation in the business.

We are essentially looking for a young, dynamic mind to provide our website with some inspiration. We encourage all designers to use their imagination and surprise us.

We have technical people to do the technical work, such as coding, but what we are looking for is asthetic creativity.

In addition, we have seen our competitors offer a translation service on their website i.e. you can just click on a flag and the website will turn into a different language. If you can incorporate this, it would be very useful.
Updates

Reason: Hi All - we have received some fantastic designs, so thank you. We are extending the deadline so that people can upgrade theirs slightly. We haven't seen enough dynamism with pictures and icons. And for those who have shown dynamism in those departments, we would also like you to consider including a video on the home page of some sort. You can find many videos of working machines like these on Clip-Spool. Thanks.

Target Market(s)

International Engineering companies

Industry/Entity Type

Flag

Requirements
Must have
• The "search database" facility must remain there.
Nice to have
• Perhaps some working videos running on the homepage of some of the types of machines we sell. You can find many such videos on ClipSpool. We will constantly change those as we get new stock in.

```html
<!DOCTYPE html>
<html lang="en">
<head>
<meta charset="utf-8">
<title>Brockway Tooling</title>
<link href="https://fonts.googleapis.com/css2?family=Questrial&family=Ubuntu:wght@400;500;700&display=swap" rel="stylesheet">
<style>
:root{
  --topbar:#353535;
  --header-top:#4a4a4a;
  --header-dark:#3c3c3c;
  --page:#ececec;
  --panel:#f7f7f7;
  --teal:#108f92;
  --ink:#3f3f3f;
  --muted:#8c8c8c;
  --body:#6a6a6a;
  --white:#ffffff;
}
*{margin:0;padding:0;box-sizing:border-box}
html,body{width:1200px;height:1174px;overflow:hidden}
body{background:var(--page);font-family:"Questrial",sans-serif;color:var(--ink);position:relative}
.topbar{position:absolute;left:0;top:0;width:1200px;height:34px;background:var(--topbar);border-bottom:1px solid #262626;font-family:"Ubuntu",sans-serif;font-size:11px;color:#c9c9c9}
.topbar .url{position:absolute;left:197px;top:11px}
.topbar .links{position:absolute;right:198px;top:11px}
.header{position:absolute;left:0;top:34px;width:1200px;height:156px;background:linear-gradient(var(--header-top),var(--header-dark))}
.logo{position:absolute;left:186px;top:22px;font-family:"Ubuntu",sans-serif;font-weight:700;font-size:28px;color:var(--white);line-height:1}
.tagline{position:absolute;right:182px;top:29px;text-align:right;color:var(--white)}
.tagline h2{font-family:"Questrial",sans-serif;font-weight:400;font-size:22px;line-height:1}
.tagline p{font-size:10px;line-height:12px;color:#e6e6e6;margin-top:1px}
.nav{position:absolute;left:180px;top:118px;width:840px;height:43px;background:linear-gradient(#fbfbfb,#dcdcdc);border-radius:3px 3px 0 0;font-family:"Ubuntu",sans-serif;font-size:11px;color:#3a3a3a}
.nav .tabs{display:flex;height:43px}
.nav a{display:flex;align-items:center;gap:6px;padding:0 0 0 12px;height:43px;border-right:1px solid #cfcfcf;text-decoration:none;color:inherit;white-space:nowrap}
.nav a.active{color:var(--teal);padding-left:16px}
.nav a.last{border-right:none}
.nav svg{flex:none}
.search{position:absolute;left:603px;top:10px;width:235px;height:25px;display:flex;background:var(--white);border-radius:2px;box-shadow:inset 0 1px 2px rgba(0,0,0,.15);overflow:hidden}
.search span{flex:1;font-size:9.5px;color:#a3a3a3;padding:7px 0 0 18px;font-family:"Ubuntu",sans-serif;white-space:nowrap;overflow:hidden}
.search button{width:39px;background:#2c2c2c;border:none;display:flex;align-items:center;justify-content:center}
.panel{position:absolute;left:180px;top:167px;width:840px;height:973px;background:var(--panel);border-radius:3px}
.slider{position:absolute;left:17px;top:15px;width:807px;height:342px;background:linear-gradient(110deg,#f4f6fb 0%,#e7ecf6 45%,#ece6ee 100%);box-shadow:0 1px 3px rgba(0,0,0,.2)}
.slide-machine{position:absolute;left:257px;top:32px;width:530px;height:265px;border-radius:4px;background:linear-gradient(90deg,#cfd2d6 0%,#c3c7cb 35%,#3aa9ac 60%,#36a3a5 85%,#d6d9dc 100%);opacity:.85}
.slide-copy{position:absolute;left:21px;top:64px;width:250px}
.slide-copy h1{font-weight:400;font-size:30px;line-height:28px;color:#3a3a3a;letter-spacing:.5px}
.slide-copy h3{font-weight:400;font-size:13px;color:var(--teal);margin-top:12px;letter-spacing:.5px}
.slide-copy p{font-size:11px;line-height:14.5px;color:var(--muted);margin-top:13px}
.btn-read{display:inline-block;margin-top:23px;background:var(--teal);color:var(--white);font-family:"Ubuntu",sans-serif;font-size:11.5px;padding:6px 9px;border-radius:2px}
.dots{position:absolute;left:363px;top:315px;display:flex;gap:6px}
.dots i{width:11px;height:11px;border-radius:50%;background:#9a9a9a;display:block}
.dots i.on{background:#333}
.welcome{position:absolute;left:28px;top:392px;width:436px}
.welcome h2{font-weight:400;font-size:16px;line-height:21px;color:#3d3d3d;letter-spacing:.3px}
.welcome p{font-size:9.5px;line-height:12.4px;color:var(--body);margin-top:12px}
.welcome h2 + p{margin-top:11px}
.works-tab{position:absolute;left:472px;top:392px;width:120px;height:31px;background:var(--teal);color:var(--white);font-size:14px;display:flex;align-items:center;justify-content:center}
.works-frame{position:absolute;left:473px;top:423px;width:324px;height:186px;background:#ececec;box-shadow:0 2px 4px rgba(0,0,0,.08)}
.video{position:absolute;left:13px;top:11px;width:300px;height:165px;background:radial-gradient(circle at 30% 55%,#4a4d52,#1f2023 55%,#0e0e10)}
.video::after{content:"";position:absolute;right:0;top:0;width:70px;height:100%;background:linear-gradient(90deg,rgba(230,232,235,0),rgba(230,232,235,.9))}
.play{position:absolute;left:135px;top:64px;width:34px;height:34px;border-radius:6px;background:rgba(20,20,20,.85);display:flex;align-items:center;justify-content:center;z-index:1}
.divider{position:absolute;left:0;top:642px;width:840px;height:1px;background:#e2e2e2}
.products h2{position:absolute;left:27px;top:671px;font-weight:400;font-size:16.5px;color:#3d3d3d;letter-spacing:.3px}
.product{position:absolute;top:708px;width:171px}
.product .photo{width:171px;height:102px}
.product h4{font-family:"Ubuntu",sans-serif;font-weight:400;font-size:10.5px;color:#3a3a3a;margin-top:14px}
.product p{font-family:"Ubuntu",sans-serif;font-size:10px;line-height:14.5px;color:#a2a2a2;margin-top:6px}
.btn-detail{display:inline-block;margin-top:6px;margin-left:1px;width:60px;height:18px;background:var(--teal);color:var(--white);font-family:"Ubuntu",sans-serif;font-size:11px;text-align:center;line-height:18px}
.footer{position:absolute;left:0;top:934px;width:840px;border-top:1px solid #e2e2e2;font-family:"Ubuntu",sans-serif;font-size:10px;color:#444}
.footer .links{position:absolute;left:16px;top:15px}
.footer .copy{position:absolute;right:17px;top:15px}
</style>
</head>
<body>
<div class="topbar">
  <span class="url">www.brockwaytooling.com</span>
  <span class="links">Enquiry | About US</span>
</div>
<header class="header">
  <div class="logo">Brockway Tooling</div>
  <div class="tagline">
    <h2>We are a global leader</h2>
    <p>in the production of new CNC machines &amp; retrofit<br>conventional machines into CNC machine tools.</p>
  </div>
</header>
<nav class="nav">
  <div class="tabs">
    <a class="active" href="#" style="width:91px"><svg width="24" height="18" viewBox="0 0 26 20"><path d="M13 1 1 11h4v8h6v-6h4v6h6v-8h4z" fill="#108f92"/></svg>Home</a>
    <a href="#" style="width:120px"><svg width="18" height="18" viewBox="0 0 20 20"><circle cx="10" cy="10" r="6.5" fill="#5a5a5a"/><g stroke="#5a5a5a" stroke-width="3"><path d="M10 1v18M1 10h18M3.6 3.6l12.8 12.8M16.4 3.6 3.6 16.4"/></g><circle cx="10" cy="10" r="2.5" fill="#e8e8e8"/></svg>Used Machines</a>
    <a href="#" style="width:145px"><svg width="29" height="18" viewBox="0 0 32 20"><g fill="#5a5a5a"><circle cx="10" cy="11" r="6"/><circle cx="24" cy="7" r="4"/></g><g stroke="#5a5a5a" stroke-width="2.5"><path d="M10 2v18M1 11h18M3.6 4.6l12.8 12.8M16.4 4.6 3.6 17.4M24 1v12M18 7h12"/></g><circle cx="10" cy="11" r="2.3" fill="#e8e8e8"/><circle cx="24" cy="7" r="1.5" fill="#e8e8e8"/></svg>New CNC Machine</a>
    <a href="#" style="width:121px"><svg width="18" height="18" viewBox="0 0 20 20"><circle cx="10" cy="10" r="8.5" fill="none" stroke="#5a5a5a" stroke-width="1.6"/><ellipse cx="10" cy="10" rx="4" ry="8.5" fill="none" stroke="#5a5a5a" stroke-width="1.3"/><path d="M2 7h16M2 13h16" stroke="#5a5a5a" stroke-width="1.3"/></svg>Manufacturing</a>
    <a class="last" href="#" style="width:100px"><svg width="18" height="18" viewBox="0 0 20 20"><circle cx="10" cy="10" r="8.5" fill="none" stroke="#5a5a5a" stroke-width="1.5"/><path d="M7 5c-1 1-1 3 1 6s4 4 5 4l1.5-1.5-2-1.8-1 .8c-1-.5-2.3-2-2.7-3l.8-1L8.6 4.5z" fill="#5a5a5a"/></svg>Contact</a>
  </div>
  <div class="search">
    <span>Type any machine name / make / model</span>
    <button aria-label="Search"><svg width="10" height="10" viewBox="0 0 10 10"><circle cx="4" cy="4" r="3" fill="none" stroke="#fff" stroke-width="1.5"/><path d="M6.2 6.2 9 9" stroke="#fff" stroke-width="1.8"/></svg></button>
  </div>
</nav>

<main class="panel">
  <section class="slider">
    <div class="slide-machine" role="img" aria-label="Photo of a large grey and teal CNC surface grinding machine"></div>
    <div class="slide-copy">
      <h1>CNC-SURFACE<br>GRINDER.</h1>
      <h3>NOW AVAILABLE</h3>
      <p>Lorem Ipsum est simplement du faux texte employés ans la composition et la mise e page avant mpression. Le Lorem Ipsum est le faux standard.</p>
      <span class="btn-read">Read More</span>
    </div>
    <div class="dots"><i class="on"></i><i></i><i></i><i></i><i></i></div>
  </section>

  <section class="welcome">
    <h2>WELCOME TO<br>BROCKWAY TOOLING</h2>
    <p>Brockway Tooling is an established vendor of new and used machine tools, with over 30 years' experience in buying, rebuilding, retrofitting and commissioning machine tools WORLDWIDE. We have industrial space both in London and Mumbai, where we store over 200 machines at any given time. We specialise in gear manufacturing,</p>
    <p>pressure diecasting, plano miller, boring and grinding machines, as well as heat treatment facilities, machining and turning centres. Such machines find their usage in the automotive, aviation, power generation, mining and construction industries. Our stock includes the industry's best brands such as Gleaver, Pfanner, Hurlin and Bauten. The stock comprises both CNC and conventional machines.</p>
    <p>We are a global leader in the production of new CNC machines, as we retrofit conventional machines into affordable CNC machine tools.</p>
  </section>

  <div class="works-tab">Our Works</div>
  <div class="works-frame">
    <div class="video" role="img" aria-label="Video still of a working machine tool with a blue hydraulic arm">
      <div class="play"><svg width="14" height="16" viewBox="0 0 14 16"><path d="M1 1l12 7-12 7z" fill="#fff"/></svg></div>
    </div>
  </div>

  <div class="divider"></div>

  <section class="products">
    <h2>OUR PRODUCTS</h2>
    <div class="product" style="left:26px">
      <div class="photo" role="img" aria-label="Photo of a green cylindrical grinder" style="background:linear-gradient(135deg,#a9cfd8,#6f9f7d 55%,#4f7358)"></div>
      <h4>Cylindrical Grinder</h4>
      <p>Lorem Ipsum est simplement du<br>faux texte employé dans la</p>
      <span class="btn-detail">Detail</span>
    </div>
    <div class="product" style="left:230px">
      <div class="photo" role="img" aria-label="Photo of a yellow cylindrical grinder" style="background:linear-gradient(120deg,#e8e020,#c9c21c 45%,#8a8d8e 70%,#b7bcbe)"></div>
      <h4>Cylindrical Grinder</h4>
      <p>Lorem Ipsum est simplement du<br>faux texte employé dans la</p>
      <span class="btn-detail" style="margin-left:3px">Detail</span>
    </div>
    <div class="product" style="left:436px">
      <div class="photo" role="img" aria-label="Photo of a long green lathe in a workshop" style="background:linear-gradient(160deg,#8c7f5d,#93b493 45%,#6f8f72)"></div>
      <h4>Cylindrical Grinder</h4>
      <p>Lorem Ipsum est simplement du<br>faux texte employé dans la</p>
      <span class="btn-detail">Detail</span>
    </div>
    <div class="product" style="left:641px">
      <div class="photo" role="img" aria-label="Photo of a large grey-green industrial grinder" style="background:linear-gradient(135deg,#5f4f3c,#7d8a76 45%,#c8c3b0)"></div>
      <h4>Cylindrical Grinder</h4>
      <p>Lorem Ipsum est simplement du<br>faux texte employé dans la</p>
      <span class="btn-detail" style="margin-left:3px">Detail</span>
    </div>
  </section>

  <footer class="footer">
    <span class="links">Home | Used Machines | New CNC Machines | Contact Us | Sitemap</span>
    <span class="copy">Copyright. Brockway Tooling. All Rights Reserved.</span>
  </footer>
</main>
</body>
</html>
```